cleaning service

we are a cleaning company,

we have a current flyer but its very dull

I have attached it, can we make it look modern, maybe add pictures and colour

```html
<!DOCTYPE html>
<html lang="en">
<head>
<meta charset="utf-8">
<title>Cleaning Services by Maple's News – Trifold Brochure</title>
<link rel="stylesheet" href="https://fonts.googleapis.com/css2?family=Arimo:wght@400;700&family=Montserrat:wght@500;600&family=Dancing+Script:wght@700&family=Roboto+Condensed:wght@700&display=swap">
<style>
:root{
  --bg:#e3e3e3;
  --gold:#c49a3a;
  --gold-light:#e8d190;
  --gold-dark:#9a7224;
  --maroon:#861544;
  --maroon-dark:#560a2b;
  --red:#c4161e;
  --cream:#fbf4de;
  --ink:#3a3a3a;
  --white:#ffffff;
}
*{box-sizing:border-box;margin:0;padding:0}
html,body{width:880px;height:1200px;overflow:hidden;background:var(--bg)}
.canvas{position:relative;width:880px;height:1200px;overflow:hidden;background:var(--bg);font-family:"Arimo",Arial,sans-serif;color:var(--ink)}
.sheet{position:absolute;left:20px;width:840px;height:570px;display:flex;background:var(--white);box-shadow:0 8px 18px rgba(0,0,0,.25)}
.sheet--outside{top:20px}
.sheet--inside{top:610px}
.panel{position:relative;width:280px;height:100%;overflow:hidden}
.panel--white{background:var(--white)}
.panel--maroon{background:radial-gradient(ellipse at 50% 40%,var(--maroon) 0%,var(--maroon-dark) 100%)}
.block{position:absolute;left:13px;right:13px}
.service-title{display:flex;align-items:center;gap:7px;font-size:10.5px;color:var(--red)}
.service-title--gold{color:var(--gold-light)}
.service-icon{width:17px;height:19px;border-radius:2px;background:var(--red);flex:none}
.service-icon--gold{background:var(--gold-light)}
.copy{margin-top:5px;font-size:6.7px;line-height:1.28;text-align:justify;color:#444}
.copy--light{color:var(--white)}
.fine{margin-top:5px;font-size:5.3px;line-height:1.22;text-align:justify;color:var(--red)}
.fine--gold{color:var(--gold-light)}
.price-table{margin-top:7px;background:var(--cream);box-shadow:0 1px 2px rgba(0,0,0,.15)}
.price-table__head{background:linear-gradient(90deg,var(--gold-light),var(--gold),var(--gold-light));color:var(--red);text-align:center;font-size:6.6px;padding:2px 0;text-transform:uppercase}
.price-table__body{padding:5px 12px 6px}
.price-row{display:grid;grid-template-columns:122px auto;font-size:6.1px;line-height:1.5;color:#222}
.pill{display:flex;justify-content:space-between;align-items:center;margin-top:6px;padding:3px 12px;border-radius:10px;background:#fffaf0;border:1px solid #e2d2a2;font-size:7.6px;color:#222}
.pill__accent{color:var(--red)}
.photo{position:absolute;left:0;right:0}
.curve{position:absolute;left:0;width:280px;display:block}
.heading-caps{font-family:"Montserrat",Arial,sans-serif;font-weight:600;color:var(--white);letter-spacing:.5px}
.script{font-family:"Dancing Script",cursive;font-weight:700;color:var(--white)}
.about__title{position:absolute;left:13px;top:30px;font-size:15px}
.about__text{position:absolute;left:13px;right:13px;top:60px;font-size:8px;line-height:1.3;text-align:justify;color:var(--white)}
.about__text p+p{margin-top:9px}
.round-photo{position:absolute;border-radius:50%;border:3px solid var(--white);box-shadow:0 0 0 3px var(--gold)}
.promo{position:absolute;left:0;right:0;text-align:center}
.promo__title{font-size:14.5px}
.promo__script{font-size:17px;margin-top:2px}
.promo__text{margin-top:14px;font-size:9.6px;line-height:1.8;color:var(--white);padding:0 16px}
.cover__title{font-size:19px}
.cover__script{font-size:25px;margin-top:2px}
.call-pill{display:inline-flex;align-items:center;gap:8px;margin-top:18px;padding:3px 16px;border-radius:12px;background:linear-gradient(90deg,var(--gold-dark),var(--gold-light),var(--gold));font-family:"Roboto Condensed",Arial,sans-serif;font-size:10.5px;color:var(--maroon-dark)}
.call-pill__phone{display:inline-flex;align-items:center;gap:4px}
.beat-price{margin-top:6px;font-family:"Roboto Condensed",Arial,sans-serif;font-size:10px;color:var(--white)}
.offer-badge{position:absolute;left:138px;top:318px;width:130px;height:90px}
.offer-badge__circle{position:absolute;left:25px;top:0;width:82px;height:82px;border-radius:50%;background:radial-gradient(circle,var(--maroon) 55%,var(--maroon-dark));border:3px solid var(--gold);box-shadow:0 0 0 2px var(--maroon-dark),0 0 0 4px var(--gold-light)}
.offer-badge__value{position:absolute;left:25px;top:14px;width:82px;text-align:center;font-family:"Montserrat",Arial,sans-serif;font-weight:600;color:var(--white);font-size:24px;line-height:1}
.offer-badge__value small{font-size:8px}
.offer-badge__ribbon{position:absolute;left:0;top:46px;width:132px;height:20px;background:linear-gradient(90deg,var(--gold-dark),var(--gold-light),var(--gold-dark));clip-path:polygon(0 0,100% 0,94% 50%,100% 100%,0 100%,6% 50%);text-align:center;font-family:"Montserrat",Arial,sans-serif;font-weight:600;font-size:10.5px;line-height:20px;color:var(--maroon-dark)}
.call-line{position:absolute;left:0;right:0;text-align:center;font-family:"Roboto Condensed",Arial,sans-serif;font-size:10px;color:#111;display:flex;justify-content:center;align-items:center;gap:8px}
</style>
</head>
<body>
<main class="canvas">

  <!-- Outside spread -->
  <section class="sheet sheet--outside">

    <div class="panel panel--white">
      <div class="block" style="top:20px">
        <h3 class="service-title"><span class="service-icon" role="img" aria-label="Curtain cleaning icon"></span>Curtain Cleaning</h3>
        <p class="copy">The cleaning specialists will use professional equipment and will wipe all washable surfaces down in order to eradicate and disinfect from all the harmful germs. Our broad spectrum and certified disinfectant is perfect for disease control or precautionary measure in any property or business, in order to ensure and maintain hygienic conditions. Our antiviral sanitisation service can be requested separately or combined with any of our other services.</p>
        <div class="price-table">
          <div class="price-table__head">Curtain cleaning</div>
          <div class="price-table__body">
            <div class="price-row"><span>Pair of curtains – half length</span><span>£24</span></div>
            <div class="price-row"><span>Pair of curtains – full length</span><span>£29</span></div>
          </div>
        </div>
      </div>
      <div class="block" style="top:195px">
        <h3 class="service-title"><span class="service-icon" role="img" aria-label="Window cleaning icon"></span>Window Cleaning</h3>
        <p class="copy">Maple's Cleaning services offers professional window cleaning services in London. Our well-trained and vetted cleaners will do a fantastic job in keeping your property's windows bright and clean, ensuring that windows, frames and sills are cleaned professionally. You can benefit from our great expertise and affordable prices for London window cleaning.</p>
      </div>
      <div class="photo" style="top:330px;bottom:0;background:linear-gradient(160deg,#eef0ec 0%,#d9dcd6 45%,#b9b3a8 100%)" role="img" aria-label="Bright dining room with white table, chairs and curtained French windows"></div>
      <svg class="curve" style="top:300px" height="70" viewBox="0 0 280 70" aria-hidden="true">
        <defs><linearGradient id="goldA" x1="0" x2="1"><stop offset="0" stop-color="#9a7224"/><stop offset=".5" stop-color="#e8d190"/><stop offset="1" stop-color="#c49a3a"/></linearGradient></defs>
        <path d="M0 0H280V16C190 30 90 58 0 50Z" fill="#fff"/>
        <path d="M0 50C90 58 190 30 280 16V24C190 40 90 66 0 60Z" fill="url(#goldA)"/>
      </svg>
    </div>

    <div class="panel panel--maroon">
      <svg class="curve" style="top:0" height="420" viewBox="0 0 280 420" aria-hidden="true">
        <defs><linearGradient id="goldB" x1="0" y1="0" x2="0" y2="1"><stop offset="0" stop-color="#b8892c"/><stop offset="1" stop-color="#c9a24a"/></linearGradient></defs>
        <path d="M0 0H280V345C200 395 100 360 0 395Z" fill="url(#goldB)"/>
        <path d="M0 395C100 360 200 395 280 345" fill="none" stroke="#fff" stroke-width="1.5"/>
      </svg>
      <h2 class="heading-caps about__title">ABOUT US</h2>
      <div class="about__text">
        <p>Maple's Cleaning Services offers professional cleaning services to make your home look its very best. From cleaning sinks, baths and tiles to polishing windows, our cleaners have the expertise to deal with every cleaning challenge.</p>
        <p>Let me customise a cleaning service programme to suit your individual needs and your budget. Whether you require a regular service (daily, weekly or monthly) or just a one-off service, you can count on Maple's Cleaning services for a cleaning service at excellent rates.</p>
        <p>In addition, Maple's Cleaning Services believes that the products we use really matter. All the products we use are natural and non-toxic, which makes them healthier for your home and safer for the local London environment. I have personally research all our house cleaning products to ensure they are non-toxic, biodegradable and not tested on animals.</p>
      </div>
      <div class="round-photo" style="left:82px;top:287px;width:114px;height:114px;background:radial-gradient(circle at 40% 40%,#d7d9dc,#8c8f95)" role="img" aria-label="Vacuum cleaner on a freshly cleaned carpet"></div>
      <div class="promo" style="top:428px">
        <h2 class="heading-caps promo__title">CLEANING SERVICES</h2>
        <p class="script promo__script">by Maple's News</p>
        <p class="promo__text">We can integrate the cleaning services with the newspaper delivery services and as well are offering a 20% off for all our newspaper customers and £50 for introducing us to your family and friends.</p>
      </div>
    </div>

    <div class="panel panel--maroon">
      <div class="photo" style="top:0;height:420px;background:linear-gradient(180deg,#9fb4c9 0%,#c7c4bb 40%,#d9c7a8 70%,#b79e7b 100%)" role="img" aria-label="Smiling family of four in front of a large suburban house"></div>
      <svg class="curve" style="top:370px" height="90" viewBox="0 0 280 90" aria-hidden="true">
        <defs><linearGradient id="goldC" x1="0" x2="1"><stop offset="0" stop-color="#c49a3a"/><stop offset=".5" stop-color="#f0dc9c"/><stop offset="1" stop-color="#9a7224"/></linearGradient></defs>
        <path d="M0 62C90 40 190 58 280 22V90H0Z" fill="#861544"/>
        <path d="M0 62C90 40 190 58 280 22" fill="none" stroke="url(#goldC)" stroke-width="4"/>
      </svg>
      <div class="offer-badge">
        <div class="offer-badge__circle"></div>
        <div class="offer-badge__value">20<small>% OFF</small></div>
        <div class="offer-badge__ribbon">SPECIAL OFFER</div>
      </div>
      <div class="promo" style="top:452px">
        <h1 class="heading-caps cover__title">CLEANING SERVICES</h1>
        <p class="script cover__script">by Maple's News</p>
        <div class="call-pill">PLEASE CALL US ON
          <span class="call-pill__phone">
            <svg width="9" height="9" viewBox="0 0 24 24" aria-hidden="true"><path d="M6.6 10.8a15 15 0 006.6 6.6l2.2-2.2c.3-.3.7-.4 1-.2 1.1.4 2.3.6 3.6.6.6 0 1 .4 1 1V20c0 .6-.4 1-1 1A17 17 0 013 4c0-.6.4-1 1-1h3.5c.6 0 1 .4 1 1 0 1.3.2 2.5.6 3.6.1.3 0 .7-.2 1z" fill="#560a2b"/></svg>07700 900123</span>
        </div>
        <p class="beat-price">TO BEAT ANY PRICE</p>
      </div>
    </div>
  </section>

  <!-- Inside spread -->
  <section class="sheet sheet--inside">

    <div class="panel panel--white">
      <div class="photo" style="top:0;height:225px;background:linear-gradient(160deg,#e9ecef 0%,#cfd4d8 50%,#9aa1a6 100%)" role="img" aria-label="Clean living room with white sofas and large windows"></div>
      <svg class="curve" style="top:178px" height="62" viewBox="0 0 280 62" aria-hidden="true">
        <defs><linearGradient id="goldD" x1="0" x2="1"><stop offset="0" stop-color="#9a7224"/><stop offset=".5" stop-color="#e8d190"/><stop offset="1" stop-color="#c49a3a"/></linearGradient></defs>
        <path d="M0 38C100 20 190 22 280 0V14C190 34 100 34 0 50Z" fill="url(#goldD)"/>
        <path d="M0 50C100 34 190 34 280 14V62H0Z" fill="#fff"/>
      </svg>
      <div class="block" style="top:244px">
        <h3 class="service-title"><span class="service-icon" role="img" aria-label="Sanitisation icon"></span>Antiviral Sanitisation Service</h3>
        <p class="copy">The cleaning specialists will use professional equipment and will wipe all washable surfaces down in order to eradicate and disinfect from all the harmful germs. Our broad spectrum and certified disinfectant is perfect for disease control or precautionary measure in any property or business, in order to ensure and maintain hygienic conditions. Our antiviral sanitisation service can be requested separately or combined with any of our other services.</p>
        <p class="fine">BS EN 1276 is the European standard for the bactericidal activity of chemical disinfectants as proof of effective infection control against harmful micro-organisms such as MRSA, Salmonella, E.Coli, Flu Virus (H1N1), HIV/AIDS, TB, SARS, Hepatitis, Influenza A. In order to pass this standard, products have been tested by an independent laboratory and must prove a bacterium kill rate of 99.999% within 5 minutes.</p>
        <div class="pill"><span>Including our cleaning materials</span><span class="pill__accent">£16 (per hour)</span></div>
      </div>
      <div class="block" style="top:424px">
        <h3 class="service-title"><span class="service-icon" role="img" aria-label="Deep cleaning icon"></span>One Off Deep Cleaning Service</h3>
        <p class="copy">If you require one-off cleaning to freshen up your home Maple's Cleaning Services can help you. We can arrange for a team of professional cleaners to come to your home at a time that's convenient for you. Our deep cleaning service is perfect for all households looking to save themselves from tiresome home spring cleaning.</p>
        <p class="fine">Our One-off service is a deep cleaning of your home, Airbnb, or holiday house in London and the nearby towns. Our cleaning team can bring cleaning solutions and equipment, or we can do the service with tools and supplies provided by you. We will work according to your requirements, and you can create a checklist with the areas you want us to clean. The service is perfect for your spring cleaning or any other general clean-up of the house.</p>
        <div class="pill"><span>Including our cleaning materials</span><span class="pill__accent">£16 (per hour)</span></div>
      </div>
    </div>

    <div class="panel panel--maroon">
      <div class="block" style="top:24px">
        <h3 class="service-title service-title--gold"><span class="service-icon service-icon--gold" role="img" aria-label="Carpet cleaning icon"></span>Carpet Cleaning</h3>
        <p class="copy copy--light">Maple's Cleaning services provides professional carpet cleaning service, carried out by our certified cleaners with years of professional experience. Our reputation speaks for itself.</p>
        <p class="fine fine--gold">We provide a high-quality deep carpet cleaning service for all types of rugs and carpets. The method we apply when tending to the textile floorings is hot water extraction, also known as steam cleaning. We also do stain removal, treating even old stubborn spots and spills on all types of rugs. With us, you can also add fabric guard stain protection service to enhance the results of the deep carpet cleaning.</p>
        <div class="price-table">
          <div class="price-table__head">Carpet cleaning</div>
          <div class="price-table__body">
            <div class="price-row"><span>Single Bedroom</span><span>£19</span></div>
            <div class="price-row"><span>Double Bedroom</span><span>£24</span></div>
            <div class="price-row"><span>Living / Dining / Lounge</span><span>£29</span></div>
            <div class="price-row"><span>Hallway</span><span>£13</span></div>
            <div class="price-row"><span>Landing</span><span>£7</span></div>
            <div class="price-row"><span>Steps</span><span>£2 ( per step )</span></div>
            <div class="price-row"><span>Bathroom</span><span>£6</span></div>
          </div>
        </div>
        <div class="pill"><span>Including our cleaning materials <span class="pill__accent">Minimum charge of £49</span></span></div>
      </div>
      <div class="round-photo" style="left:30px;top:243px;width:86px;height:86px;background:radial-gradient(circle,#d8e4ee,#6e8fb0)" role="img" aria-label="Gloved hand cleaning a window"></div>
      <div class="round-photo" style="left:98px;top:235px;width:92px;height:92px;background:radial-gradient(circle,#e6e2dc,#9a948b)" role="img" aria-label="Steam cleaning a carpet"></div>
      <div class="round-photo" style="left:170px;top:243px;width:86px;height:86px;background:radial-gradient(circle,#f1e7b8,#b6a054)" role="img" aria-label="Cleaning a surface with a yellow cloth"></div>
      <div class="block" style="top:340px">
        <h3 class="service-title service-title--gold"><span class="service-icon service-icon--gold" role="img" aria-label="Rug cleaning icon"></span>Rug Cleaning</h3>
        <p class="copy copy--light">Maple's Cleaning services offers professional rug cleaning service at competitive prices! Book our skilled technicians and have your textile floorings impeccably cleaned in no time. We will bring the as-new look of any rug, including antique rugs, Persian rugs, area rugs and more. If you need us to deal with a nasty stain or any other accident on your rug, you can now book our emergency rug cleaning service for a same-day appointment at no extra cost!</p>
      </div>
      <div class="block" style="top:450px">
        <h3 class="service-title service-title--gold"><span class="service-icon service-icon--gold" role="img" aria-label="Oven cleaning icon"></span>Oven Cleaning <span style="color:var(--white)">From £42</span></h3>
        <p class="copy copy--light">Maple's Cleaning services offers professional oven cleaning service at competitive prices! Book our skilled technicians and have your kitchen appliances impeccably cleaned in no time. We will bring back the as-new look of any oven, including range cookers, hobs and extractor hoods. If you need us to deal with burnt-on grease or any other accident in your kitchen, you can now book our emergency cleaning service for a same-day appointment at no extra cost!</p>
        <p class="fine fine--gold">Maple's Cleaning services provides professional oven cleaning in all London boroughs. You can hire us to clean the stove in your home or restaurant. We will remove the grease and burnt food from hob or the gas burners; we will clean the appliance inside and out, including the door and the racks.</p>
      </div>
    </div>

    <div class="panel panel--white">
      <div class="block" style="top:24px">
        <h3 class="service-title"><span class="service-icon" role="img" aria-label="Upholstery cleaning icon"></span>Upholstery Cleaning</h3>
        <p class="copy">Keeping your home clean is vital and taking care of upholstery is an important part of that. If you're struggling to find time around the demands of family and/or career, Maple's Cleaning services can help.</p>
        <div class="price-table">
          <div class="price-table__head">Upholstery cleaning</div>
          <div class="price-table__body">
            <div class="price-row"><span>Armchair</span><span>£17</span></div>
            <div class="price-row"><span>Two seater sofa</span><span>£22</span></div>
            <div class="price-row"><span>Three seater sofa</span><span>£32</span></div>
            <div class="price-row"><span>Four seater sofa</span><span>£42</span></div>
            <div class="price-row"><span>Dining chair</span><span>£6</span></div>
          </div>
        </div>
        <p class="fine">Our upholstery cleaning team is focused on delivering an outstanding result when treating your sofa or armchairs. We can also clean loveseats, dining chairs, ottomans and other types of furnishings. We clean various types of upholstery, including natural materials like leather, wool, and suede, as well as fibre blends, or human-made fibres and materials such as microfiber, faux fur and leather.</p>
        <div class="pill"><span>Including our cleaning materials <span class="pill__accent">Minimum charge of £49</span></span></div>
      </div>
      <div class="block" style="top:228px">
        <h3 class="service-title"><span class="service-icon" role="img" aria-label="Mattress cleaning icon"></span>Mattress Cleaning</h3>
        <p class="copy">Maple's Cleaning Services provides mattress cleaning for your residential property in. Our technicians use safe but efficient solutions and powerful professional equipment to remove dirt, dust, and bacteria from your bedding. We can deal with all kinds of stains on your mattress and will restore its as-new look at an inexpensive price.</p>
        <div class="price-table">
          <div class="price-table__head">Mattress cleaning</div>
          <div class="price-table__body">
            <div class="price-row"><span>Single Mattress both sides</span><span>£19</span></div>
            <div class="price-row"><span>Double Mattress both sides</span><span>£29</span></div>
          </div>
        </div>
      </div>
      <p class="call-line" style="top:360px">PLEASE CALL US ON
        <svg width="10" height="10" viewBox="0 0 24 24" aria-hidden="true"><path d="M6.6 10.8a15 15 0 006.6 6.6l2.2-2.2c.3-.3.7-.4 1-.2 1.1.4 2.3.6 3.6.6.6 0 1 .4 1 1V20c0 .6-.4 1-1 1A17 17 0 013 4c0-.6.4-1 1-1h3.5c.6 0 1 .4 1 1 0 1.3.2 2.5.6 3.6.1.3 0 .7-.2 1z" fill="#111"/></svg>07700 900123</p>
      <div class="photo" style="top:410px;bottom:0;background:linear-gradient(160deg,#e7e5e2 0%,#cfcac3 55%,#a79f94 100%)" role="img" aria-label="Tidy bedroom with a neatly made bed and upholstered headboard"></div>
      <svg class="curve" style="top:380px" height="70" viewBox="0 0 280 70" aria-hidden="true">
        <defs><linearGradient id="goldE" x1="0" x2="1"><stop offset="0" stop-color="#c49a3a"/><stop offset=".5" stop-color="#e8d190"/><stop offset="1" stop-color="#9a7224"/></linearGradient></defs>
        <path d="M0 0H280V0C200 30 110 52 0 46Z" fill="#fff"/>
        <path d="M0 46C110 52 200 30 280 0V18C200 46 110 64 0 58Z" fill="url(#goldE)"/>
      </svg>
    </div>
  </section>

</main>
</body>
</html>
```